THE HOMESTEAD LEDGER
STATIONARY, ENVELOPES, FLYERS, BUSINESS CARDS
Project: THE HOMESTEAD LEDGER
THE HOMESTEAD LEDGER - Real Estate
Creative Brief
Professional
MALCOLM J. VANTREASE
PRINCIPAL BROKER
518 WILLOWCREST DRIVE CEDAR HOLLOW, KENTUCKY 40999
malcolmvantrease@quillmail.example
FRONT SIDE DESIGN AND/OR LOGO WITH INDIVIDUAL INFORMATION AND AREA FOR INDIVIDUAL PICTURE.
AT LEAST "THE HOMESTEAD LEDGER" LOGO. OPEN TO OTHER DESIGN AND/OR BORDERS WITH IT.

```html
<!DOCTYPE html>
<html lang="en">
<head>
<meta charset="utf-8">
<title>The Homestead Ledger – Business Cards</title>
<link href="https://fonts.googleapis.com/css2?family=Libre+Baskerville:wght@400;700&display=swap" rel="stylesheet">
<style>
  :root{
    --backdrop:#4a3528;
    --paper:#ffffff;
    --olive-light:#c9c28e;
    --olive:#a9a065;
    --olive-deep:#7c7340;
    --silver-light:#eeeeee;
    --silver-dark:#9a9a9a;
    --ink:#4b4b40;
    --on-olive:#ffffff;
  }
  *{margin:0;padding:0;box-sizing:border-box}
  html,body{width:1200px;height:732px;overflow:hidden}
  body{background:var(--backdrop);font-family:"Libre Baskerville",serif;position:relative}

  .card{position:absolute;width:295px;height:516px;overflow:hidden;
    box-shadow:0 6px 18px rgba(0,0,0,.35)}
  .card--front{left:281px;top:62px;border-radius:18px 18px 4px 18px;
    background:radial-gradient(ellipse at 50% 55%,var(--olive-light) 0%,var(--olive) 55%,var(--olive-deep) 100%)}
  .card--back{left:629px;top:154px;border-radius:18px 4px 18px 18px;
    background:radial-gradient(ellipse at 45% 45%,var(--olive-light) 0%,var(--olive) 55%,var(--olive-deep) 100%)}

  .front-wave{position:absolute;left:0;top:0;width:295px;height:240px}

  .brand{position:absolute;left:0;width:100%;text-align:center;color:var(--ink);
    font-weight:700;line-height:1.15;letter-spacing:.06em}
  .card--front .brand{top:84px;font-size:19px}
  .card--back .brand{top:226px;font-size:23px}

  .holder{position:absolute;left:0;width:100%;text-align:center;color:var(--on-olive)}
  .holder__name{top:246px;font-size:16px;letter-spacing:.02em}
  .holder__title{top:275px;font-size:10px;letter-spacing:.05em}

  .portrait{position:absolute;left:109px;top:314px;width:77px;height:91px;
    background:var(--paper);box-shadow:0 0 3px rgba(0,0,0,.25)}

  .contact{position:absolute;left:0;top:434px;width:100%;text-align:center;
    color:var(--on-olive);font-size:7.4px;line-height:13px;letter-spacing:.02em;font-style:normal}
</style>
</head>
<body>

<section class="card card--front" aria-label="Business card front">
  <svg class="front-wave" viewBox="0 0 295 240" aria-hidden="true">
    <defs>
      <linearGradient id="silver" x1="0" y1="0" x2="1" y2="0">
        <stop offset="0" stop-color="#9a9a9a"/>
        <stop offset=".45" stop-color="#eeeeee"/>
        <stop offset="1" stop-color="#9a9a9a"/>
      </linearGradient>
    </defs>
    <path d="M0 0H295V182C240 160 190 200 130 212C80 222 35 214 0 206Z" fill="url(#silver)"/>
    <path d="M0 0H295V172C240 152 190 190 130 200C80 208 35 200 0 192Z" fill="#ffffff"/>
  </svg>

  <div class="brand">THE HOMESTEAD<br>LEDGER</div>

  <p class="holder holder__name">MALCOLM J. VANTREASE</p>
  <p class="holder holder__title">PRINCIPAL BROKER</p>

  <div class="portrait" role="img" aria-label="Space for the broker's portrait photo"></div>

  <address class="contact">
    518 WILLOWCREST DRIVE,<br>
    CEDAR HOLLOW, KENTUCKY 40999<br>
    cell: 270-555-0143<br>
    e-mail: malcolmvantrease@quillmail.example
  </address>
</section>

<section class="card card--back" aria-label="Business card back">
  <div class="brand">THE HOMESTEAD<br>LEDGER</div>
</section>

</body>
</html>
```